New Word Template Design Project

I need this document for death certificate ordering to look like our branding. I will attach the pdf with the information and a sample pdf of our style. I also think that check boxes and x's would be better than yes and no.

2nd page in spanish.

Industry/Entity Type

Funeral

Requirements
Should not have
• Check boxes and red x's or yellow next to the yes, no , or sometimes

```html
<!DOCTYPE html>
<html lang="en">
<head>
<meta charset="utf-8">
<title>Death Certificate Ordering Guide – Hartwell Funeral &amp; Cremation Services</title>
<link href="https://fonts.googleapis.com/css2?family=Jost:wght@400;500;600&display=swap" rel="stylesheet">
<style>
  :root {
    --ink: #1c1c1c;
    --navy: #234a68;
    --blue: #4b84a6;
    --lilac: #9a90c2;
    --gold: #d4a637;
    --rule: #b9b9c4;
    --paper: #ffffff;
  }
  * { margin: 0; padding: 0; box-sizing: border-box; }
  html, body { width: 927px; height: 1200px; overflow: hidden; background: var(--paper); }
  body { font-family: "Jost", "Futura", sans-serif; color: var(--ink); position: relative; }

  .brand {
    position: absolute; right: 60px; top: 52px;
    display: flex; align-items: center; gap: 8px;
    font-size: 34px; font-weight: 500; color: var(--blue);
  }
  .brand-dot { width: 12px; height: 12px; border-radius: 50%; background: var(--blue); }

  .doc-title { position: absolute; left: 57px; top: 82px; font-size: 28.5px; font-weight: 500; color: var(--navy); letter-spacing: 0.1px; }
  .doc-sub { position: absolute; left: 57px; font-size: 16.5px; font-weight: 400; }
  .doc-sub.guide { top: 136px; }
  .doc-sub.county { top: 172px; }

  .intro { position: absolute; left: 58px; top: 220px; width: 814px; font-size: 13.3px; line-height: 18.2px; }

  .uses {
    position: absolute; left: 57px; top: 296px; width: 815px;
    border-collapse: collapse; font-size: 13.8px; table-layout: fixed;
  }
  .uses thead tr { background: linear-gradient(90deg, var(--blue) 0%, var(--lilac) 55%, var(--gold) 100%); color: #fff; }
  .uses th { height: 27px; font-weight: 500; font-size: 14px; text-align: center; }
  .uses th.use { text-align: left; padding-left: 15px; }
  .uses td { height: 27.4px; border: 1px solid var(--rule); padding: 0 13px; white-space: nowrap; }
  .uses td.qty { text-align: center; }
  .uses td.small { font-size: 11.8px; }
  .mark { display: inline-flex; align-items: center; gap: 10px; padding-left: 2px; }
  .mark svg { width: 16px; height: 16px; flex: none; }

  .notes { position: absolute; left: 58px; top: 750px; width: 815px; font-size: 13.3px; line-height: 18.2px; }
  .notes p { margin-bottom: 18px; }
  .notes strong { font-weight: 600; }
  .notes h3 { font-size: 13.3px; font-weight: 600; }
  .notes ul { list-style: none; margin-bottom: 18px; }
  .notes li { position: relative; padding-left: 26px; }
  .notes li::before { content: ""; position: absolute; left: 2px; top: 5px; width: 9px; height: 9px; border-radius: 50%; background: var(--blue); }

  .footer-band { position: absolute; left: 0; bottom: 0; width: 927px; height: 22px; background: linear-gradient(90deg, var(--blue), var(--lilac) 55%, var(--gold)); }
</style>
</head>
<body>
<svg width="0" height="0" style="position:absolute">
  <defs>
    <symbol id="icon-check" viewBox="0 0 16 16">
      <rect x="0.5" y="0.5" width="15" height="15" rx="3" fill="#4b84a6"/>
      <path d="M3.8 8.3l2.7 2.7 5.7-6" fill="none" stroke="#fff" stroke-width="2" stroke-linecap="round" stroke-linejoin="round"/>
    </symbol>
    <symbol id="icon-cross" viewBox="0 0 16 16">
      <path d="M2.5 2.5l11 11M13.5 2.5l-11 11" stroke="#d4a637" stroke-width="2.6" stroke-linecap="round"/>
    </symbol>
  </defs>
</svg>

<div class="brand"><span class="brand-dot"></span>Hartwell</div>

<h1 class="doc-title">Hartwell Funeral &amp; Cremation Services</h1>
<p class="doc-sub guide">Death Certificate Ordering Guide</p>
<p class="doc-sub county">Miami-Dade County</p>

<p class="intro">Certified death certificates are used to handle legal, financial, and personal matters after a loved one passes. While some institutions require an original, others may only need to view or copy it. In Florida, you can order death certificates <strong><em>with</em></strong> or <strong><em>without</em></strong> the cause of death. Cause of death is confidential and should only be included when necessary.</p>

<table class="uses">
  <colgroup><col style="width:325px"><col style="width:163px"><col style="width:162px"><col style="width:165px"></colgroup>
  <thead>
    <tr><th class="use">Use</th><th>Original Needed?</th><th>With Cause?</th><th>Suggested Quantity</th></tr>
  </thead>
  <tbody>
    <tr><td>Life Insurance Claims</td><td><span class="mark"><svg><use href="#icon-check"/></svg>Yes</span></td><td><span class="mark"><svg><use href="#icon-check"/></svg>Yes</span></td><td class="qty">1 per policy</td></tr>
    <tr><td>Pension or Retirement Benefits</td><td><span class="mark"><svg><use href="#icon-check"/></svg>Yes</span></td><td><span class="mark"><svg><use href="#icon-check"/></svg>Yes</span></td><td class="qty">1</td></tr>
    <tr><td>Bank Accounts</td><td><span class="mark"><svg><use href="#icon-cross"/></svg>Usually Not</span></td><td><span class="mark"><svg><use href="#icon-cross"/></svg>No</span></td><td class="qty">0–1</td></tr>
    <tr><td>Investment / Brokerage Accounts</td><td><span class="mark"><svg><use href="#icon-check"/></svg>Sometimes</span></td><td><span class="mark"><svg><use href="#icon-check"/></svg>Sometimes</span></td><td class="qty">1–2</td></tr>
    <tr><td>Vehicle Title Transfer (DMV)</td><td><span class="mark"><svg><use href="#icon-check"/></svg>Yes</span></td><td><span class="mark"><svg><use href="#icon-cross"/></svg>No</span></td><td class="qty">1</td></tr>
    <tr><td>Property / Real Estate Transfers</td><td><span class="mark"><svg><use href="#icon-check"/></svg>Yes</span></td><td><span class="mark"><svg><use href="#icon-cross"/></svg>No</span></td><td class="qty">1 per property</td></tr>
    <tr><td>Probate / Court Matters</td><td><span class="mark"><svg><use href="#icon-check"/></svg>Yes</span></td><td><span class="mark"><svg><use href="#icon-check"/></svg>Often</span></td><td class="qty">1–2</td></tr>
    <tr><td>Social Security / Government Benefits</td><td><span class="mark"><svg><use href="#icon-cross"/></svg>No</span></td><td><span class="mark"><svg><use href="#icon-cross"/></svg>No</span></td><td class="qty">0</td></tr>
    <tr><td>Passport Cancellation / Consulates</td><td><span class="mark"><svg><use href="#icon-check"/></svg>Yes</span></td><td><span class="mark"><svg><use href="#icon-check"/></svg>Yes</span></td><td class="qty">1</td></tr>
    <tr><td>Domestic Travel with &nbsp;&nbsp;&nbsp; Cremated Remains</td><td><span class="mark"><svg><use href="#icon-check"/></svg>Yes</span></td><td><span class="mark"><svg><use href="#icon-cross"/></svg>No</span></td><td class="qty">1</td></tr>
    <tr><td class="small">International Travel with &nbsp;&nbsp;&nbsp;&nbsp; Cremated Remains</td><td><span class="mark"><svg><use href="#icon-check"/></svg>Yes</span></td><td><span class="mark"><svg><use href="#icon-check"/></svg>Sometimes</span></td><td class="qty">1</td></tr>
    <tr><td>Domestic Forwarding of Remains</td><td><span class="mark"><svg><use href="#icon-check"/></svg>Yes</span></td><td><span class="mark"><svg><use href="#icon-cross"/></svg>No</span></td><td class="qty">1</td></tr>
    <tr><td>International Forwarding of Remains</td><td><span class="mark"><svg><use href="#icon-check"/></svg>Yes</span></td><td><span class="mark"><svg><use href="#icon-check"/></svg>Yes</span></td><td class="qty">1</td></tr>
    <tr><td>Credit Cards / Utility Companies</td><td><span class="mark"><svg><use href="#icon-cross"/></svg>Usually Not</span></td><td><span class="mark"><svg><use href="#icon-cross"/></svg>No</span></td><td class="qty">0</td></tr>
    <tr><td>Personal Copy / Peace of Mind</td><td><span class="mark"><svg><use href="#icon-cross"/></svg>Optional</span></td><td><span class="mark"><svg><use href="#icon-check"/></svg>Optional</span></td><td class="qty">1</td></tr>
  </tbody>
</table>

<section class="notes">
  <h3>Pricing (Miami-Dade County):</h3>
  <p>The first certified death certificate is <strong><em>$20</em></strong>, and each additional copy is <strong><em>$16</em></strong>.</p>
  <p>If you are <strong>traveling domestically</strong> or <strong>internationally with cremated remains</strong>, at least one certified copy is typically required. Some countries may require the certificate <strong>with cause of death.</strong> We will reach out to the consulate of the destination country to confirm the specific requirements for transporting cremated remains.</p>
  <p>Please note: <strong>Other counties may have different pricing</strong> for death certificates. We will inform you of the exact cost based on the location of death.</p>
  <p><strong>Most families order 4 to 8 certified copies.</strong> A mix is common — for example, 2 with cause and 4 without cause. It simpler and more cost-effective to order them at the time of need. If you're unsure, we are here to guide you through the process.</p>
  <h3>How many certified copies would you like to order?</h3>
  <ul>
    <li>With Cause of Death</li>
    <li>Without Cause of Death</li>
  </ul>
  <h3>Questions? We're Here for You</h3>
  <ul>
    <li>(305) 555-0142</li>
    <li>kendall@hartwellfuneral.com | midtown@hartwellfuneral.com | coralgables@hartwellfuneral.com | preplanning@hartwellfuneral.com Serving Miami-Dade County with care, dignity, and support for over 100 years.</li>
  </ul>
</section>

<div class="footer-band"></div>
</body>
</html>
```